Brightmark Pixel Collective Website

I need my website redesigned to look very modern with the latest services. Check out my old website for information: www.brightmarkpixelcollective.com

You can use the same site menu links

It doesn't need to have the Recent News section

Please use the yellow, black and grey color scheme

Target Market(s)

25-50 years in range. Small Business Owners

Industry/Entity Type

Group

Requirements
Must have
• Logo and similar color scheme to current website
• Modern, Modern, Modern! I want a very fresh and modern look
Should not have
• Boring Look

```html
<!DOCTYPE html>
<html lang="en">
<head>
<meta charset="utf-8">
<title>Brightmark Pixel Collective</title>
<link href="https://fonts.googleapis.com/css2?family=Arimo:wght@400;700&family=Lato:wght@400;700&display=swap" rel="stylesheet">
<style>
:root{
  --yellow:#fbb619;
  --yellow-soft:#f6c243;
  --gold:#d9a52a;
  --black:#111111;
  --ink:#1b1b1b;
  --grey:#4a4a4a;
  --white:#ffffff;
}
*{margin:0;padding:0;box-sizing:border-box}
html,body{width:1200px;height:2870px;overflow:hidden;background:var(--white)}
body{position:relative;font-family:"Lato",Arial,sans-serif;color:var(--ink)}
.abs{position:absolute}

/* hero */
.hero{left:0;top:0;width:1200px;height:883px;
  background:radial-gradient(ellipse at 70% 35%,#dfe8f2 0%,#b9cbe0 30%,transparent 60%),
  radial-gradient(ellipse at 30% 75%,#c9a58e 0%,transparent 45%),
  linear-gradient(160deg,#9fb2c9 0%,#d8dde4 45%,#a8938a 80%,#7a6a66 100%)}
.nav{left:240px;top:22px;display:flex;gap:14px}
.nav a{width:132px;height:127px;background:var(--yellow);color:var(--black);text-decoration:none;
  display:flex;flex-direction:column;align-items:center;justify-content:center;gap:14px;
  font-size:17px}
.nav a.active{background:#1c1c1c;color:var(--yellow)}
.nav svg{width:44px;height:44px}
.brand{left:0;top:420px;width:1200px;display:flex;align-items:center;justify-content:center;gap:22px}
.brand-mark{width:56px;height:56px;background:var(--yellow)}
.brand-name{font-family:"Lato",sans-serif;font-size:50px;font-weight:400;color:#3a3a3a;letter-spacing:1px}
.cta{left:468px;top:751px;width:264px;height:67px;background:#151515;border-radius:4px;
  display:flex;align-items:center;justify-content:center;gap:22px;color:var(--white);font-size:19px}
.cta svg{width:32px;height:32px}

/* separators */
.rule{left:0;width:1200px}
.arrow{left:569px;width:0;height:0;border-left:31px solid transparent;border-right:31px solid transparent}

/* section heads */
.head-icon{left:557px;width:86px;height:86px;border-radius:50%;background:var(--yellow);
  display:flex;align-items:center;justify-content:center}
.head-icon svg{width:40px;height:40px}
.head-title{left:0;width:1200px;text-align:center;font-family:"Arimo",Arial,sans-serif;font-weight:700;
  font-size:44px;color:var(--black);letter-spacing:-1px}
.tagline{left:420px;width:360px;height:44px;background:var(--yellow);color:var(--black);
  display:flex;align-items:center;justify-content:center;font-size:17px;box-shadow:0 4px 0 #e9e3d2}
.tagline::before{content:"";position:absolute;left:172px;top:-9px;border-left:8px solid transparent;
  border-right:8px solid transparent;border-bottom:9px solid var(--yellow)}

/* about */
.about-band{left:0;top:1272px;width:1200px;height:583px;
  background:linear-gradient(180deg,var(--gold) 0%,#e8b63a 50%,var(--yellow-soft) 100%)}
.about-copy{left:160px;top:1334px;width:880px;text-align:center;font-size:15.5px;line-height:28px;color:#1e1a10}
.team{left:160px;top:1498px;display:flex;gap:45px}
.member{width:185px;height:280px;background:var(--black);color:var(--white);text-align:center}
.member-photo{width:185px;height:129px;background:linear-gradient(180deg,#d9d9d9,#8a8a8a)}
.member-name{margin-top:29px;font-size:16px}
.member-role{margin-top:10px;font-size:13px}
.socials{margin-top:14px;display:flex;justify-content:center;gap:7px}
.socials span{width:26px;height:26px;border-radius:50%;background:var(--yellow)}

/* services */
.services-band{left:0;top:2239px;width:1200px;height:545px;
  background:radial-gradient(ellipse at 75% 20%,#3a3a3a 0%,transparent 55%),linear-gradient(180deg,#1d1d1d,#262626 60%,#1a1a1a)}
.service{top:2311px;width:260px;height:401px;background:var(--white);border-top:5px solid var(--yellow);text-align:center}
.service-icon{margin:28px auto 0;width:130px;height:130px;border-radius:50%;background:var(--yellow);
  display:flex;align-items:center;justify-content:center}
.service-icon svg{width:58px;height:58px}
.service h3{margin-top:22px;font-family:"Arimo",Arial,sans-serif;font-size:17px;line-height:22px;color:var(--black)}
.service hr{width:110px;margin:12px auto 0;border:0;border-top:2px solid var(--yellow)}
.service p{margin:16px 18px 0;font-size:13.5px;line-height:17px;color:var(--grey);text-align:left}
.service a{display:inline-block;margin-top:22px;width:110px;height:32px;line-height:30px;border:1px solid #999;
  font-size:12px;color:var(--black);text-decoration:none}
</style>
</head>
<body>

<div class="abs hero" role="img" aria-label="Blurred photo of business people working at a desk"></div>

<nav class="abs nav">
  <a class="active" href="#">
    <svg viewBox="0 0 24 24" fill="currentColor"><path d="M12 3 2 12h3v9h5v-6h4v6h5v-9h3z"/></svg>Home</a>
  <a href="#">
    <svg viewBox="0 0 24 24" fill="currentColor"><circle cx="12" cy="7" r="4"/><path d="M4 22c0-5 3.5-8 8-8s8 3 8 8z"/><path d="M11 14h2l.6 6-1.6 1.5L10.4 20z" fill="#fbb619"/></svg>About us</a>
  <a href="#">
    <svg viewBox="0 0 24 24" fill="currentColor"><path d="M9 4h6v3h6v13H3V7h6zm2 0v3h2V4z"/></svg>Services</a>
  <a href="#">
    <svg viewBox="0 0 24 24" fill="currentColor"><path d="M3 7h4l2-3h6l2 3h4v13H3z"/><circle cx="12" cy="13" r="4" fill="#fbb619"/><circle cx="12" cy="13" r="2.3"/></svg>Portfolio</a>
  <a href="#">
    <svg viewBox="0 0 24 24" fill="currentColor"><path d="M16 3l5 5L9 20H4v-5z"/></svg>Contact us</a>
</nav>

<div class="abs brand">
  <span class="brand-mark"></span>
  <span class="brand-name">Brightmark Pixel Collective</span>
</div>

<a class="abs cta">
  <svg viewBox="0 0 24 24" fill="#fbb619"><path d="M3 5h11v2H5v12h12v-8h2v10H3z"/><path d="M18 2l4 4-9 9H9v-4z"/></svg>
  Request a Free Estimate
</a>

<div class="abs rule" style="top:883px;height:10px;background:var(--yellow)"></div>
<div class="abs arrow" style="top:893px;border-top:33px solid var(--yellow)"></div>

<!-- About -->
<div class="abs head-icon" style="top:999px">
  <svg viewBox="0 0 24 24" fill="#111"><circle cx="12" cy="7" r="4"/><path d="M4 22c0-5 3.5-8 8-8s8 3 8 8z"/></svg>
</div>
<h2 class="abs head-title" style="top:1096px">ABOUT</h2>
<div class="abs tagline" style="top:1154px">Lorem Ipsum is simply dummy text of the</div>

<section class="abs about-band" role="img" aria-label="Faint photo of team members over a yellow wash"></section>
<div class="abs arrow" style="top:1272px;border-top:33px solid var(--white)"></div>
<p class="abs about-copy">Contrary to popular belief, Lorem Ipsum is not simply random text. It has roots in a piece of classical Latin literature from 45 BC, making it over 2000 years old. Harold Wenfield, a Latin professor at Ashgrove College in Vermont, looked up one of the more obscure Latin words, consectetur, from a Lorem Ipsum passage, and going through the cites of the word in classical literature, discovered the undoubtable source. Lorem Ipsum comes from sections 1.10.32 and 1.10.</p>

<div class="abs team">
  <div class="member">
    <div class="member-photo" role="img" aria-label="Portrait photo of lena mors"></div>
    <div class="member-name">lena mors</div>
    <div class="member-role">CEO</div>
    <div class="socials"><span></span><span></span><span></span></div>
  </div>
  <div class="member">
    <div class="member-photo" role="img" aria-label="Portrait photo of Tomas"></div>
    <div class="member-name">Tomas</div>
    <div class="member-role">Web Designer</div>
    <div class="socials"><span></span><span></span><span></span></div>
  </div>
  <div class="member">
    <div class="member-photo" role="img" aria-label="Portrait photo of Ravi Delgado"></div>
    <div class="member-name">Ravi Delgado</div>
    <div class="member-role">Online Marketing Expert</div>
    <div class="socials"><span></span><span></span><span></span></div>
  </div>
  <div class="member">
    <div class="member-photo" role="img" aria-label="Portrait photo of Owen"></div>
    <div class="member-name">Owen</div>
    <div class="member-role">Graphic Designer</div>
    <div class="socials"><span></span><span></span><span></span></div>
  </div>
</div>

<div class="abs rule" style="top:1853px;height:14px;background:var(--black)"></div>
<div class="abs arrow" style="top:1867px;border-top:26px solid var(--black)"></div>

<!-- Services -->
<div class="abs head-icon" style="top:1959px">
  <svg viewBox="0 0 24 24" fill="#111"><path d="M9 4h6v3h6v13H3V7h6zm2 0v3h2V4z"/></svg>
</div>
<h2 class="abs head-title" style="top:2058px">SERVICES</h2>
<div class="abs tagline" style="top:2117px">Lorem Ipsum is simply dummy text of the</div>

<section class="abs services-band" role="img" aria-label="Dark photo of a workspace"></section>
<div class="abs arrow" style="top:2239px;border-top:33px solid var(--white)"></div>

<div class="abs service" style="left:160px">
  <div class="service-icon">
    <svg viewBox="0 0 24 24" fill="#111"><path d="M10.5 2h3l.5 2.6 1.9.8 2.2-1.5 2.1 2.1-1.5 2.2.8 1.9 2.5.4v3l-2.5.5-.8 1.9 1.5 2.2-2.1 2.1-2.2-1.5-1.9.8-.5 2.5h-3l-.5-2.5-1.9-.8-2.2 1.5-2.1-2.1 1.5-2.2-.8-1.9L2 13.5v-3l2.5-.4.8-1.9-1.5-2.2 2.1-2.1 2.2 1.5 1.9-.8zM12 8.5a3.5 3.5 0 1 0 0 7 3.5 3.5 0 0 0 0-7z"/></svg>
  </div>
  <h3>Web site Design and<br>Development</h3>
  <hr>
  <p>Contrary to popular belief, Lorem Ipsum is not simply random text. It has roots in a piece of classical Latin literature from 45 BC, making it over 2000 years old.</p>
  <a href="#">Learn more</a>
</div>

<div class="abs service" style="left:470px">
  <div class="service-icon">
    <svg viewBox="0 0 24 24" fill="#111"><path d="M7 6h10c3 0 5 3 5 7s-1 5-2.5 5c-2 0-3-3-5-3h-5c-2 0-3 3-5 3C3 18 2 17 2 13s2-7 5-7z"/><path d="M6 10h1.3v1.3h1.3v1.4H7.3V14H6v-1.3H4.7v-1.4H6z" fill="#fbb619"/><circle cx="17" cy="10.5" r="1" fill="#fbb619"/><circle cx="18.6" cy="12.5" r="1" fill="#fbb619"/></svg>
  </div>
  <h3>Graphic and print<br>Design</h3>
  <hr>
  <p>Contrary to popular belief, Lorem Ipsum is not simply random text. It has roots in a piece of classical Latin literature from 45 BC, making it over 2000 years old.</p>
  <a href="#">Learn more</a>
</div>

<div class="abs service" style="left:778px">
  <div class="service-icon">
    <svg viewBox="0 0 24 24" fill="none" stroke="#111" stroke-width="2"><circle cx="12" cy="12" r="9"/><path d="M3 12h18M12 3c3 3 3 15 0 18M12 3c-3 3-3 15 0 18M5 7.5h14M5 16.5h14"/></svg>
  </div>
  <h3>Search engine<br>Marketing</h3>
  <hr>
  <p>Contrary to popular belief, Lorem Ipsum is not simply random text. It has roots in a piece of classical Latin literature from 45 BC, making it over 2000 years old.</p>
  <a href="#">Learn more</a>
</div>

<div class="abs rule" style="top:2784px;height:12px;background:var(--yellow)"></div>
<div class="abs arrow" style="top:2796px;border-top:30px solid var(--yellow)"></div>

</body>
</html>
```